Digital Billboard Design: Winter Sales Event

I own a boutique furniture store in Calgary, AB (maplewoven.ca) and I am looking to advertise our winter sale event on a new curved digital billboard (specs attached including required file type).

I have this billboard rented for 52-weeks so I will be looking to change the design every 4-weeks (i.e. this is intended to be an ongoing project).

The objective of this first billboard is to raise awareness around our annual winter sales event. The store itself is only a few blocks from the billboard so those commuting into downtown are just a short drive from the store.

I am looking for a fresh, clean, contemporary look that will grab your attention as you drive into downtown Calgary without presenting to much info so as to be distracting (and overwhelming -- the billboard does not need to contain all info on my current marketing material). I should also note that the store caters to a higher-end, more sophisticated clientele so the graphics need to reflect the brand (i.e. we are not Brenton Furniture or Couch Depot!).

I have attached three files:

Billboard specs
Current marketing material advertising sale (and all relevant data)
An idea that is from an American furniture store that I think is interesting

Target Market(s)

Upper middle class, sophisticated client who appreciates the finer things in life.

Industry/Entity Type

Furniture Store

Font styles to use
Sans Serif

Requirements
Must have
• Company Logo
• Winter Sales Event - 20 to 60% off
• Address: 3847 22nd Ave SW
Nice to have
• Image of furniture -- see our website www.maplewoven.ca -- any photo from this site can be used
Should not have
• Too much text or visual distration

```html
<!DOCTYPE html>
<html lang="en">
<head>
<meta charset="utf-8">
<title>Maple Woven – Winter Sales Event Billboard</title>
<link rel="stylesheet" href="https://fonts.googleapis.com/css2?family=Rajdhani:wght@700&family=Questrial&display=swap">
<style>
  :root {
    --sky-blue: #81b7d4;
    --frost-blue: #b4d5e7;
    --frame-blue: #3d9fcc;
    --edge-blue: #b6dcee;
    --snow-white: #ffffff;
    --ink-dark: #3a3a3c;
    --ink-body: #2b2b2b;
    --page-white: #ffffff;
  }
  * { box-sizing: border-box; margin: 0; padding: 0; }
  html, body {
    width: 1200px;
    height: 1000px;
    overflow: hidden;
    background: var(--page-white);
  }
  .canvas {
    position: relative;
    width: 1200px;
    height: 1000px;
    border: 1px solid var(--edge-blue);
    background: var(--page-white);
  }
  .billboard {
    position: absolute;
    left: 150px;
    top: 278px;
    width: 900px;
    height: 433px;
    border: 1px solid var(--frame-blue);
  }
  .promo-panel {
    position: relative;
    height: 328px;
    background: var(--sky-blue);
  }
  .snowfall {
    position: absolute;
    left: 158px;
    top: 0;
    width: 130px;
    height: 186px;
    background: var(--frost-blue);
    border-radius: 0 0 6px 6px;
  }
  .headline {
    position: absolute;
    left: 24px;
    top: 196px;
    font-family: "Rajdhani", sans-serif;
    font-weight: 700;
    color: var(--snow-white);
    line-height: 1;
  }
  .headline-title {
    font-size: 68px;
    letter-spacing: 4px;
  }
  .headline-offer {
    display: inline-block;
    margin-top: 8px;
    font-size: 56px;
    letter-spacing: 9px;
  }
  .store-panel {
    height: 103px;
    background: var(--page-white);
    display: flex;
    flex-direction: column;
    align-items: center;
    justify-content: center;
    gap: 8px;
    font-family: "Questrial", sans-serif;
  }
  .store-name {
    font-size: 44px;
    letter-spacing: 5px;
    color: var(--ink-dark);
    line-height: 1;
  }
  .store-address {
    font-size: 33px;
    letter-spacing: 4px;
    color: var(--ink-body);
    line-height: 1;
  }
</style>
</head>
<body>
  <main class="canvas">
    <section class="billboard">
      <div class="promo-panel">
        <div class="snowfall" role="img" aria-label="Cluster of white snowflakes falling from the top edge"></div>
        <h1 class="headline">
          <span class="headline-title">WINTER SALES EVENT</span><br>
          <span class="headline-offer">20 TO 60% OFF</span>
        </h1>
      </div>
      <footer class="store-panel">
        <p class="store-name">MAPLE WOVEN</p>
        <p class="store-address">3847 22nd Ave SW, CALGARY, AB.</p>
      </footer>
    </section>
  </main>
</body>
</html>
```